Corvo Pizza & Pasta dual-restaurant promotional flyer

I would like to do a tri-fold flyer to promote my two restaurants located close to each other and help concierges understand the subtle differences between them. I have done a mock in powerpoint but it is 300+MB so i took pics of my mock to attach and will attach the separate pictures and text. i would like it put into a proper flyer template and get help to clean up the design, particularly the flyer header which should show either i) our CORVO PIZZA and CORVO PASTA logo or ii) show CORVO logo and then have the words Corvo Pizza Corvo Pasta below it (in non-logo). I have the logo files in vector and pdf too if that is better. I need help to photoshop the logos to work with the flyer and clean up overall design. The pages which shows the restaurant contact details is also a little hard to read in the current layout. Open to all changes.

Industry/Entity Type

Restaurant

Requirements
Must have
• Front page - must feature both logos and both restaurants photos (that i show on my uploaded draft flyer)
• All photos must be used
Nice to have
• I have uploaded a draft flyer of what i am trying to achieve
Should not have
• The feel should be warm and personable.

```html
<!DOCTYPE html>
<html lang="en">
<head>
<meta charset="utf-8">
<title>Corvo Pizza &amp; Pasta – Tri-fold Inside</title>
<link href="https://fonts.googleapis.com/css2?family=Roboto:wght@400;700&family=Parisienne&display=swap" rel="stylesheet">
<style>
  :root{
    --bg-dark:#2a1a15;
    --bg-mid:#3b2820;
    --gold:#f5c22b;
    --ring:#d8a93c;
    --text:#f4ede6;
  }
  html,body{margin:0;padding:0;overflow:hidden;background:var(--bg-dark);}
  .flyer{
    position:relative;width:1200px;height:848px;overflow:hidden;
    background:linear-gradient(180deg,var(--bg-dark) 0%,var(--bg-mid) 55%,var(--bg-dark) 100%);
    font-family:"Roboto",Arial,sans-serif;color:var(--text);
  }
  .heading{
    position:absolute;margin:0;font-weight:700;font-size:20px;letter-spacing:1px;
    color:var(--gold);text-align:center;
  }
  .body-copy{
    position:absolute;margin:0;font-size:12.5px;line-height:25.6px;letter-spacing:.1px;
    white-space:nowrap;
  }
  .body-copy p{margin:0 0 25.6px;}
  .food-heading{left:0;width:385px;top:24px;}
  .food-copy{left:13px;top:60px;}
  .photo-circle{position:absolute;}
  .middle-art{position:absolute;left:397px;top:0;}
  .quote{
    position:absolute;left:420px;top:320px;width:385px;margin:0;
    font-size:20px;line-height:25.6px;letter-spacing:.6px;color:var(--gold);
  }
  .quote-mark{position:absolute;left:404px;top:320px;font-size:22px;font-weight:700;color:var(--gold);}
  .attribution{
    position:absolute;right:405px;top:405px;margin:0;text-align:right;
    font-family:"Parisienne",cursive;font-size:19px;line-height:24px;color:var(--gold);
  }
  .wines-heading{left:810px;width:385px;top:402px;}
  .wines-copy{left:832px;top:441px;}
  .pours{position:absolute;left:834px;top:590px;width:350px;border-collapse:collapse;font-size:13px;}
  .pours th{font-weight:400;color:var(--gold);font-size:14.5px;text-align:center;padding:0 0 10px;}
  .pours th.label{text-align:left;}
  .pours td{padding:0;height:25.6px;vertical-align:top;text-align:center;}
  .pours td.wine{text-align:left;white-space:nowrap;}
  .pours .indent{padding-left:12px;}
  .beers-title{position:absolute;left:834px;top:764px;margin:0;font-size:14.5px;color:var(--gold);font-weight:400;}
  .beers-list{position:absolute;left:835px;top:794px;margin:0;font-size:13px;letter-spacing:.2px;}
</style>
</head>
<body>
<div class="flyer">

  <h2 class="heading food-heading">OUR FOOD</h2>
  <div class="body-copy food-copy">
    <p>We are famed for our huge selection of white &amp; red pizzas,<br>
    among which our Pizza Corvo Pizza, Mascarpone Pizza and<br>
    Pizza Apetitosa are some of the most popular choices. Our<br>
    pizza dough is handmade fresh daily and topped with only the<br>
    freshest ingredients. For instance, a discerning palate will tell<br>
    that we only use top-grade salami.</p>
    <p>We can go on for hours about our pizzas but there are many<br>
    other deserving items on our menu like our Risotto al Funghi,<br>
    Rigatoni Sicilliana, and Parpadelle Boscoiala. The pizzeria also<br>
    features pasta dishes but Corvo Pasta’s menu is deliberately<br>
    more extensive with a wide selection of seafood and meat<br>
    options as well. Corvo Pizza’s pies can also be ordered at Corvo<br>
    Pasta.</p>
    <p>If you would like something sweet to finish, our creamy Tiramisu<br>
    and our Vanilla Bean Pannacotta never fail to deliver.</p>
  </div>

  <svg class="photo-circle" style="left:5px;top:510px" width="204" height="198" role="img" aria-label="Photo: seafood spaghetti with prawns and clams">
    <defs><radialGradient id="g-seafood" cx="50%" cy="50%" r="60%"><stop offset="0" stop-color="#e36a2a"/><stop offset=".7" stop-color="#c4411d"/><stop offset="1" stop-color="#e9dccf"/></radialGradient></defs>
    <circle cx="102" cy="99" r="96" fill="url(#g-seafood)" stroke="var(--ring)" stroke-width="5"/>
  </svg>
  <svg class="photo-circle" style="left:176px;top:638px" width="210" height="210" role="img" aria-label="Photo: pappardelle with meat ragout and mushrooms">
    <defs><radialGradient id="g-pappardelle" cx="50%" cy="50%" r="60%"><stop offset="0" stop-color="#c96a45"/><stop offset=".7" stop-color="#a94a2d"/><stop offset="1" stop-color="#eee6dc"/></radialGradient></defs>
    <circle cx="105" cy="105" r="101" fill="url(#g-pappardelle)" stroke="var(--ring)" stroke-width="5"/>
  </svg>

  <svg class="middle-art" width="413" height="848" viewBox="0 0 413 848">
    <defs>
      <linearGradient id="g-salad" x1="0" y1="0" x2="1" y2="1"><stop offset="0" stop-color="#e9e3d6"/><stop offset=".35" stop-color="#4f7a2c"/><stop offset=".7" stop-color="#2f5a1c"/><stop offset="1" stop-color="#e8e6e2"/></linearGradient>
      <linearGradient id="g-ham" x1="0" y1="0" x2="0" y2="1"><stop offset="0" stop-color="#e9d6d2"/><stop offset=".3" stop-color="#b75f5d"/><stop offset=".75" stop-color="#a04846"/><stop offset="1" stop-color="#d9c9b8"/></linearGradient>
    </defs>
    <rect x="0" y="0" width="413" height="4" fill="var(--ring)"/>
    <path d="M0 4 H413 V232 C330 272 180 264 100 252 C50 245 20 246 0 248 Z" fill="url(#g-salad)" role="img" aria-label="Photo: spinach salad with feta, orange and pine nuts"/>
    <path d="M0 248 C20 246 50 245 100 252 C180 264 330 272 413 232" fill="none" stroke="var(--ring)" stroke-width="4"/>
    <path d="M0 522 C60 516 120 506 200 507 C290 508 360 518 413 530 V848 H0 Z" fill="url(#g-ham)" role="img" aria-label="Photo: prosciutto draped over grilled flatbread"/>
    <path d="M0 522 C60 516 120 506 200 507 C290 508 360 518 413 530" fill="none" stroke="var(--ring)" stroke-width="4"/>
    <rect x="0" y="844" width="413" height="4" fill="var(--ring)"/>
  </svg>

  <span class="quote-mark">“</span>
  <p class="quote">You must go to Corvo Pizza, They have<br>really good Italian food but DO NOT<br>BLOG about it!</p>
  <p class="attribution">-Marcus Teo a.k.a celebrity blogger<br>Lady Copper Spoon</p>

  <svg class="photo-circle" style="left:992px;top:12px" width="206" height="206" role="img" aria-label="Photo: pizza with spinach, cheese and cured meat">
    <defs><radialGradient id="g-pizza" cx="50%" cy="50%" r="60%"><stop offset="0" stop-color="#e8c9a0"/><stop offset=".6" stop-color="#b8623e"/><stop offset="1" stop-color="#4a3a2a"/></radialGradient></defs>
    <circle cx="103" cy="103" r="99" fill="url(#g-pizza)" stroke="var(--ring)" stroke-width="5"/>
  </svg>
  <svg class="photo-circle" style="left:827px;top:174px" width="210" height="210" role="img" aria-label="Photo: grilled lobster and calamari with lemon">
    <defs><radialGradient id="g-lobster" cx="50%" cy="50%" r="60%"><stop offset="0" stop-color="#efe6d8"/><stop offset=".6" stop-color="#d9b48c"/><stop offset="1" stop-color="#c0673b"/></radialGradient></defs>
    <circle cx="105" cy="105" r="101" fill="url(#g-lobster)" stroke="var(--ring)" stroke-width="5"/>
  </svg>

  <h2 class="heading wines-heading">OUR WINES</h2>
  <div class="body-copy wines-copy">
    <p>We offer a carefully curated selection of well-known Italian<br>
    and new world wines at excellent value and take pride in<br>
    offering really good quality, generous house pours. For those<br>
    who prefer beers and spirits,&nbsp; there is also a wide selection<br>
    so do drop in for a early drink by the river!</p>
  </div>

  <table class="pours">
    <thead>
      <tr><th class="label">House Pours</th><th>Gls</th><th>Carafe</th><th>Bot</th></tr>
    </thead>
    <tbody>
      <tr><td class="wine">Montepulciano, Colle Rosso</td><td>12</td><td>30</td><td>55</td></tr>
      <tr><td class="wine">Chianti Classico, Poggio Alto</td><td>15</td><td>41</td><td>74</td></tr>
      <tr><td class="wine">Pinot Grigio, Ca’ Luna</td><td>12</td><td>30</td><td>55</td></tr>
      <tr><td class="wine">Sauvignon Blanc. Stone Creek<br><span class="indent">Marlborough</span></td><td>15</td><td>39</td><td>72</td></tr>
    </tbody>
  </table>

  <h3 class="beers-title">Beers by bottle</h3>
  <p class="beers-list">Ferrano, Blancwater, Kaito, Valdora, Lynx</p>
</div>
</body>
</html>
```